Hipster Hard Apple Cider - Bike / Gear / Cog Themed Label

Hard Apple Cider Label Needed:

- Looking for a retro, fun, funky, Venice Beach vibe.

- Design should incorporate bike/bicycle/wheel elements, appeal to both sexes and should be applicable to a can. (See can example in attachments).

- There should be a main brand logo that can stand alone in representing the brand and the feel of the brand. I envision a bike wheel, Sp*kes, gears, etc.

Please use brand name posted as JPG titled "Brand Name" in Attached Files:
>>> Tw*n* C*d*r

Target Market(s)

Our consumer is:
- Millennial
- Hipster
- Adventurous
- Active (biking/cycling)
- A craft beer + wine purchaser
- Unisex, veering towards masculine (65% male)

Industry/Entity Type

Wheel

Requirements
Must have
• - Bike elements that tie in the brand name (cogs, sp*kes, gears, bike frame, etc.)
• - A strong logo that can represent the brand

```html
<!DOCTYPE html>
<html lang="en">
<head>
<meta charset="utf-8">
<title>Twine Cider – Hard Apple Cider Label</title>
<link href="https://fonts.googleapis.com/css2?family=Oswald:wght@400;500;700&family=Kaushan+Script&display=swap" rel="stylesheet">
<style>
  :root {
    --bg: #ffffff;
    --brown: #4f3026;
    --brown-light: #6a4337;
    --brown-dark: #3b2219;
    --orange: #ee6a1e;
    --gold: #e3a622;
    --cream: #f3e6d6;
  }
  * { margin: 0; padding: 0; box-sizing: border-box; }
  html, body {
    width: 1200px; height: 960px; overflow: hidden;
    background: var(--bg);
  }
  .canvas { position: relative; width: 1200px; height: 960px; }
  .label {
    position: absolute; top: 80px; width: 456px; height: 800px;
    overflow: hidden;
    background: linear-gradient(90deg, var(--brown-dark) 0%, var(--brown) 18%, var(--brown-light) 45%, var(--brown) 75%, var(--brown-dark) 100%);
    font-family: "Oswald", sans-serif;
  }
  .label--front { left: 110px; }
  .label--back { left: 640px; }
  .stripes { position: absolute; inset: 0; }
  .brand-mark {
    position: absolute; display: flex; align-items: center; gap: 8px;
    transform: translate(-50%, -50%);
    color: var(--orange); font-weight: 700; font-size: 26px; line-height: 1;
    letter-spacing: 1px; text-transform: uppercase; white-space: nowrap;
  }
  .brand-mark__dot {
    width: 18px; height: 18px; border-radius: 50%; background: var(--orange);
  }
  .script {
    position: absolute; font-family: "Kaushan Script", cursive;
    color: var(--gold); white-space: nowrap; line-height: 1;
    transform: translate(-50%, -50%) rotate(-16deg);
  }
  .script--hard { left: 140px; top: 390px; font-size: 64px; }
  .script--cider { left: 262px; top: 672px; font-size: 110px; }
  .apple-block {
    position: absolute; left: 60px; top: 468px; width: 330px;
    transform: skewY(-22deg); transform-origin: left top;
  }
  .apple-block__rule { height: 4px; background: var(--orange); margin: 5px 0; }
  .apple-block__rule--thin { height: 2px; }
  .apple-word {
    display: block; text-align: center;
    font-weight: 700; font-size: 116px; line-height: 1.02;
    color: var(--orange); letter-spacing: 0;
    text-shadow: 4px 3px 0 var(--gold);
  }
  .volume {
    position: absolute; left: 272px; top: 764px;
    color: var(--cream); font-size: 15px; font-weight: 500;
  }
  .warning {
    position: absolute; left: 0; right: 0; top: 402px;
    text-align: center; color: var(--orange); text-transform: uppercase;
  }
  .warning__title { font-size: 22px; font-weight: 500; margin-bottom: 22px; }
  .warning__text { font-size: 14.5px; line-height: 21px; margin-bottom: 20px; }
  .producer {
    position: absolute; left: 0; right: 0; top: 740px;
    text-align: center; color: var(--gold); text-transform: uppercase;
    font-size: 15px; font-weight: 500; line-height: 22px;
  }
</style>
</head>
<body>
<main class="canvas">

  <section class="label label--front" aria-label="Front of can">
    <svg class="stripes" width="456" height="800" viewBox="0 0 456 800" aria-hidden="true">
      <g stroke="var(--gold)" stroke-width="4">
        <line x1="0" y1="122" x2="210" y2="202"/>
        <line x1="0" y1="133" x2="206" y2="212"/>
        <line x1="0" y1="144" x2="202" y2="222"/>
        <line x1="420" y1="276" x2="456" y2="290"/>
        <line x1="416" y1="286" x2="456" y2="301"/>
        <line x1="412" y1="296" x2="456" y2="312"/>
      </g>
    </svg>
    <div class="brand-mark" style="left:306px; top:252px;">
      <span class="brand-mark__dot"></span>Twine Cider Co.
    </div>
    <span class="script script--hard">Hard</span>
    <div class="apple-block">
      <div class="apple-block__rule"></div>
      <span class="apple-word">APPLE</span>
      <div class="apple-block__rule"></div>
      <div class="apple-block__rule apple-block__rule--thin"></div>
    </div>
    <span class="script script--cider">Cider</span>
    <p class="volume">7% ALC. / 330 ML</p>
  </section>

  <section class="label label--back" aria-label="Back of can">
    <svg class="stripes" width="456" height="800" viewBox="0 0 456 800" aria-hidden="true">
      <g stroke="var(--gold)" stroke-width="4">
        <line x1="0" y1="292" x2="40" y2="278"/>
        <line x1="0" y1="303" x2="44" y2="288"/>
        <line x1="0" y1="314" x2="48" y2="298"/>
        <line x1="270" y1="196" x2="456" y2="124"/>
        <line x1="274" y1="206" x2="456" y2="135"/>
        <line x1="278" y1="216" x2="456" y2="146"/>
      </g>
    </svg>
    <div class="brand-mark" style="left:160px; top:250px;">
      <span class="brand-mark__dot"></span>Twine Cider Co.
    </div>
    <div class="warning">
      <h2 class="warning__title">Government Warning:</h2>
      <p class="warning__text">(1) According to the Surgeon General,<br>women should not drink alcoholic beverages<br>during pregnancy because of the risk<br>of birth defects.</p>
      <p class="warning__text">(2) Consumption of alcoholic beverages impairs<br>your ability to drive a car or operate machinery,<br>and may cause health problems.</p>
      <p class="warning__text">Contains sulfites</p>
    </div>
    <p class="producer">Vinted + Bottled by<br>Twine Cider Millbrook, CA</p>
  </section>

</main>
</body>
</html>
```